Commercial Web Site for software product

Ledgerly is a GDPR compliant Membership, Contact Management & List Management solution. It is an ideal replacement for any organisation or company still using spreadsheets, email clients, simple database or paper-based system to manage contact data, mail lists, and other personal information.
The target market will be Clubs/Associations in the EU.
The design will need to be a fluid design and suitable for mobile devices. The home page will contain most of the web site content, enabling a user to scroll through all the relevant information on one page. There will be a single sub page design required for supporting information.
The web site will need to support two language versions - English and German (Language selection option required). However, the build requirements will be for a static HTML site (no database) in English only. We will duplicate and make the German version ourselves.
The attached document is the first draft of the home page content. Whilst it is a little wordy, it should convey the main information that we wish to get across.
Please note: We would prefer not to use photographs for the main imagery, we feel vector graphics would be a better option . As a guide, the following design: https://en.pixelvane.example/profiles/Marlowe/designs/5502147 may provide an insight into how we imagine the home page working and contains all the key elements we would expect to be covered.
The logo contained in the attached document can be split into a logo and text. Feel free to use only the logo (without text) or separate and place the text alongside etc., We do not want to change the logo, however, how you chose to use it is up to you.
Colour's are also optional. We like the blue, but are open to alternative ideas.
The testimonials section, should contain all the questions (3) and several of the associated answers shown. Questions/Answers may be separated into speech bubbles or similar. Not all answers will be used, but are there to provide some content.
The sub pages will be used to provide background on the GDPR requirements, our Service Offering, About Us (possibly), and a contact page.
Updates
The design budget is now guaranteed.
Whilst we have no intention not to move forward with this project, I understand the 'lack of commitment' from our side may be a negative.
Once we have reviewed all submissions - we will decide upon our preferred submission.
We will only request changes from one or two designers, and will make it clear how many other designers are in the running. This I believe is fair, as you probably need this information before deciding whether to submit any changes requested!
My hope is we have a home page that enables a visitor to clearly understand what we are offering, without having to drill down into various sub pages or sections to understand the basics. I appreciate we need to write appropriate content, but the design itself should feel uncluttered and fluid.
Hopefully some of you really talented designers can throw some ideas into the pot. The concept is more important than the detail.
Thanks for considering this project.
Coding
Number of Pages Required
Font styles to use
Colors
Look and feel

```html
<!DOCTYPE html>
<html lang="en">
<head>
<meta charset="utf-8">
<title>Ledgerly – GDPR Compliant Membership</title>
<link rel="stylesheet" href="https://fonts.googleapis.com/css2?family=Plus+Jakarta+Sans:wght@600;700;800&family=Poppins:ital,wght@0,400;0,500;0,600;1,400&display=swap">
<style>
:root{
  --hero-top:#1a10a8;
  --hero-bottom:#0a0878;
  --accent:#f9a825;
  --navy:#0d0b4a;
  --muted:#8888a6;
  --band:#ececf2;
  --soft:#f3f3f6;
  --blob:#f1f1f8;
  --footer:#1b2131;
  --brand-blue:#2f74d8;
  --white:#ffffff;
}
*{box-sizing:border-box;margin:0;padding:0}
html,body{width:1200px;height:1200px;overflow:hidden;background:var(--white)}
body{position:relative;font-family:"Poppins",sans-serif;color:var(--navy)}
.page{position:absolute;left:484px;top:29px;width:1528px;height:7352px;transform:scale(0.15625);transform-origin:0 0;background:var(--white);overflow:hidden}
.abs{position:absolute}
.heading{font-family:"Plus Jakarta Sans",sans-serif;font-weight:700;color:var(--navy)}
.btn{position:absolute;background:var(--accent);color:var(--navy);font-weight:600;display:flex;align-items:center;justify-content:center;border-radius:6px}
.art{position:absolute;border-radius:40px}

/* hero */
.hero{position:absolute;left:0;top:0;width:1528px;height:812px;background:linear-gradient(160deg,var(--hero-top),var(--hero-bottom))}
.nav-mark{left:140px;top:34px;display:flex;align-items:center;gap:12px;color:var(--white);font-weight:600;font-size:26px}
.nav-mark i{width:26px;height:26px;background:var(--brand-blue);display:block}
.nav-links{left:400px;top:52px;display:flex;gap:40px;color:var(--white);font-size:16px;font-weight:500}
.nav-login{left:1168px;top:52px;color:var(--white);font-size:16px;font-weight:600}
.nav-cta{left:1252px;top:40px;width:148px;height:48px;font-size:14px}
.hero-kicker{left:128px;top:196px;color:#c9c7ee;font-size:15px;letter-spacing:2px;line-height:22px;font-weight:500}
.hero-title{left:128px;top:252px;color:var(--white);font-size:54px;line-height:66px}
.hero-desc{left:128px;top:472px;width:700px;color:#d6d4f3;font-size:11px;line-height:16px}
.hero-desc p+p{margin-top:8px}
.hero-cta{left:128px;top:596px;width:172px;height:44px;font-size:13px}

/* partners */
.partners{position:absolute;left:0;top:812px;width:1528px;height:168px;background:var(--band)}
.partner{position:absolute;top:70px;transform:translateX(-50%);white-space:nowrap;color:#3a3a5c;font-weight:600;font-size:22px}

/* feature lists */
.checklist{position:absolute;list-style:none;font-size:23px;color:var(--muted)}
.checklist li{position:relative;padding-left:48px;height:49px;line-height:49px;white-space:nowrap}
.checklist li::before{content:"";position:absolute;left:8px;top:8px;width:12px;height:24px;border-right:6px solid var(--navy);border-bottom:6px solid var(--navy);transform:rotate(40deg)}
.checklist.roomy li{height:61px;line-height:61px}
.checklist.roomy li::before{top:14px}
.blob{position:absolute;background:var(--blob);border-radius:50%}

.section-title{font-size:58px}

.band{position:absolute;left:0;width:1528px;background:var(--band);text-align:center}
.band .heading{font-size:60px;line-height:70px}
.band p{color:var(--navy)}

/* challenges */
.challenges{position:absolute;left:0;top:3752px;width:1528px;height:940px;background:var(--soft)}
.challenges .heading{position:absolute;left:128px;top:64px;font-size:60px;line-height:76px}
.challenges .copy{position:absolute;left:128px;top:244px;width:1272px;font-size:23px;line-height:30px;color:#5a5a78}
.challenges .copy p+p{margin-top:32px}

/* data */
.data-copy{left:128px;top:4940px;width:660px;font-size:21px;line-height:28px;color:#5a5a78}
.data-copy p+p{margin-top:28px}

/* testimonial */
.card{position:absolute;left:288px;top:5848px;width:952px;height:472px;border:3px solid #b9b9c9;border-radius:16px;background:var(--white);text-align:center}
.card .mark{font-family:"Plus Jakarta Sans",sans-serif;font-weight:800;font-size:120px;line-height:100px;margin-top:30px;color:var(--navy)}
.card .question{width:820px;margin:30px auto 0;font-size:22px;line-height:28px;font-weight:500}
.card .answer{width:840px;margin:44px auto 0;font-size:16px;line-height:22px;font-style:italic;color:var(--muted)}
.arrow{position:absolute;width:80px;height:80px}

/* footer */
.footer{position:absolute;left:0;top:6400px;width:1528px;height:952px}
.footer svg.wave{position:absolute;left:0;top:0}
.foot-mark{left:338px;top:176px;width:44px;height:44px;background:var(--brand-blue)}
.foot-name{left:222px;top:262px;font-size:46px;font-weight:500;color:var(--brand-blue);line-height:56px}
.foot-address{left:292px;top:476px;font-size:21px;line-height:32px;color:#d7dae3}
.foot-phone{left:292px;top:654px;font-size:18px;color:#d7dae3}
.foot-rule{width:2px;height:260px;background:#4a5064}
.foot-col h4{font-size:20px;font-weight:600;color:var(--white);margin-bottom:18px}
.foot-col a{display:block;font-size:14px;line-height:35px;color:#9ea3b5;text-decoration:none}
.social{position:absolute;top:822px;width:36px;height:36px;border-radius:50%;background:#e8eaf0}
</style>
</head>
<body>
<div class="page">

  <!-- Hero -->
  <header class="hero">
    <div class="abs nav-mark"><i></i>Ledgerly</div>
    <nav class="abs nav-links"><span>Products</span><span>Industries</span><span>Resources</span><span>About</span><span>Why Us</span><span>Contact Us</span></nav>
    <span class="abs nav-login">Log In</span>
    <span class="btn nav-cta">Request Demo</span>
    <div class="abs hero-kicker">Contact Management &amp;<br>List Management Solution</div>
    <h1 class="abs heading hero-title">Ledgerly<br>is a GDPR Compliant<br>Membership</h1>
    <div class="abs hero-desc">
      <p>Ideal replacement for any organisation or company still using spreadsheets, email clients, simple database or paper-based system to manage contact data, mail lists and other personal information.</p>
      <p>Ledgerly offers a fast, secure, GDPR compliant solution for managing and coordinating all your Membership and Contact data, and generating GDPR Compliant Marketing lists.</p>
    </div>
    <span class="btn hero-cta">Request Demo</span>
    <div class="art" role="img" aria-label="Illustration of browser windows, documents and a security shield" style="left:840px;top:192px;width:560px;height:380px;background:radial-gradient(ellipse at 55% 45%,#e9ecfb 0%,#9fb0f0 45%,rgba(26,16,168,0) 72%)"></div>
  </header>

  <!-- Partners -->
  <section class="partners">
    <span class="partner" style="left:204px">Northvale Review</span>
    <span class="partner" style="left:412px;font-size:18px">Halcyon Secure</span>
    <span class="partner" style="left:608px">Corvane</span>
    <span class="partner" style="left:784px">Tablewise</span>
    <span class="partner" style="left:972px">Reachloop</span>
    <span class="partner" style="left:1140px;font-size:18px">Sentrafy</span>
    <span class="partner" style="left:1316px;font-size:16px">Harbor Ledger</span>
  </section>

  <!-- Standard functionality -->
  <div class="blob" style="left:-120px;top:1000px;width:700px;height:760px;opacity:.7"></div>
  <h2 class="abs heading section-title" style="left:148px;top:1168px">Standard Functionality</h2>
  <ul class="checklist" style="left:160px;top:1288px">
    <li>Attendance registration &amp; management</li>
    <li>Time recording</li>
    <li>Relationship management</li>
    <li>Tasks/To-Do's</li>
    <li>Notes/history</li>
    <li>Document storage</li>
    <li>Donation Management</li>
    <li>Prospect Management</li>
    <li>Centralized, secure permission-based access</li>
    <li>GDPR compliant storage of all contact data</li>
  </ul>
  <div class="art" role="img" aria-label="Illustration of a person at a desk logging in on a large phone screen with a shield" style="left:820px;top:1324px;width:580px;height:428px;background:radial-gradient(ellipse at 50% 50%,#8b6cf0 0%,#c9c0f5 40%,rgba(255,255,255,0) 72%)"></div>

  <div class="blob" style="left:800px;top:1960px;width:900px;height:920px"></div>
  <div class="art" role="img" aria-label="Illustration of a person working with cloud settings and a laptop" style="left:140px;top:2004px;width:540px;height:568px;background:radial-gradient(ellipse at 45% 50%,#4a5ae8 0%,#b8bff4 42%,rgba(255,255,255,0) 72%)"></div>
  <ul class="checklist" style="left:820px;top:2040px">
    <li>Attendance registration &amp; management</li>
    <li>Time recording</li>
    <li>Relationship management</li>
    <li>Tasks/To-Do's</li>
    <li>Notes/history</li>
    <li>Document storage</li>
    <li>Donation Management</li>
    <li>Prospect Management</li>
    <li>Centralized, secure permission-based access</li>
    <li>GDPR compliant storage of all contact data</li>
  </ul>

  <!-- Full-service -->
  <section class="band" style="top:2772px;height:188px">
    <h2 class="heading" style="margin-top:34px">Full-Service Provision</h2>
    <p style="font-size:26px;margin-top:4px">We provide a full service for our clients, including:</p>
  </section>
  <ul class="checklist roomy" style="left:168px;top:3034px">
    <li>Installation, configuration and set-up of main system</li>
    <li>Optional Customized-Development work</li>
    <li>Data Preparation</li>
    <li>Full training</li>
    <li>Technical support</li>
    <li>Consultancy</li>
    <li>Spreadsheets, email, databases etc</li>
    <li>Importation of data</li>
    <li>Compliant with GDPR requirements</li>
  </ul>
  <div class="art" role="img" aria-label="Illustration of a support agent with headset at a laptop among plants" style="left:740px;top:3092px;width:640px;height:432px;background:radial-gradient(ellipse at 50% 55%,#2a6fd6 0%,#c3cbe6 40%,rgba(255,255,255,0) 72%)"></div>

  <!-- Challenges -->
  <section class="challenges">
    <h2 class="heading">Challenges<br>Most Organizations Encounter:</h2>
    <div class="copy">
      <p>One of the biggest challenges faced when moving from a manual record keeping system (spreadsheets, email clients, simple database, or paper etc.) is how to manage, and coordinate all the various silos of information, to arrive at a single, valid 'source of truth.</p>
      <p>We can help you identify the sources of data you need to consider, and bring all your digital records together in a single de-duplicated list. This Master Data can be cleaned and categorized to show Opt-In preferences and areas of interest to assist with profiling/segmentation for future Mail lists.</p>
      <p>The Master Data will be returned for approval, and once agreed, will be imported for you with the necessary access permissions assigned; ready for you to start using the system from day one.</p>
      <p>Paper records, typically need to be entered manually, however, these records can also be organized to minimize duplication. We advise clients to enter this data themselves. This serves as a practical training exercise to familiarize your team with how the system works, and establish confidence. Operators working with manual systems quickly see how Ledgerly helps them establish a centralized source of truth, greatly reducing the effort required to find information, and avoid the duplication - so often encountered with manual spreadsheet, email and paper-based processes.</p>
    </div>
    <span class="btn" style="left:128px;top:816px;width:148px;height:40px;font-size:11px">Request Demo</span>
  </section>

  <!-- Data storage -->
  <h2 class="abs heading" style="left:128px;top:4832px;font-size:54px">Where is the data stored?</h2>
  <div class="abs data-copy">
    <p>We provide a fully hosted service within an ISO certified European Data Centre. This can be accessed 24 hours a day, from anywhere you have internet access.</p>
    <p>Our service provides all the necessary technologies, server operating systems, database servers and SSL certificates etc., to ensure you can start using the system without requiring additional technical support to set-up and configure your own server.</p>
    <p>Clients that wish to use their own infrastructure can do so. However, they will be responsible for the supply, installation and on-going maintenance of all infrastructures. We will of course fully support the Ledgerly software.</p>
  </div>
  <div class="art" role="img" aria-label="Isometric illustration of server racks on glowing platforms" style="left:840px;top:4812px;width:620px;height:600px;background:radial-gradient(ellipse at 50% 50%,#2b62d9 0%,#a9d2f2 40%,rgba(255,255,255,0) 72%)"></div>

  <!-- Testimonials -->
  <section class="band" style="top:5560px;height:180px">
    <h2 class="heading" style="margin-top:34px">Client Testimonials</h2>
    <p style="font-size:20px;margin-top:2px">This is what our clients said to our questions about Ledgerly.</p>
  </section>
  <svg class="arrow" style="left:128px;top:6044px" viewBox="0 0 80 80" aria-hidden="true"><circle cx="40" cy="40" r="36" fill="none" stroke="#7a7a90" stroke-width="4"/><path d="M56 40H24M36 27 23 40l13 13" fill="none" stroke="#7a7a90" stroke-width="4"/></svg>
  <svg class="arrow" style="left:1320px;top:6044px" viewBox="0 0 80 80" aria-hidden="true"><circle cx="40" cy="40" r="36" fill="none" stroke="#7a7a90" stroke-width="4"/><path d="M24 40h32M44 27l13 13-13 13" fill="none" stroke="#7a7a90" stroke-width="4"/></svg>
  <article class="card">
    <div class="mark">“</div>
    <p class="question">What is the main benefit/output of the program for you? (Which functions make your work easier and why?</p>
    <p class="answer">Attendance list tablet - simple overview of present children.<br>Note function - easy and fast recording of important notes about the child, as well as practical search function. I love the ability to notify other staff about notes - allows for transparent, quick and easy sharing of important information.<br>Capturing contact details - makes work easier - the search function allows you to quickly find relevant contact details, e.g. emergency contact numbers in case of an emergency.</p>
  </article>

  <!-- Footer -->
  <footer class="footer">
    <svg class="wave" width="1528" height="952" viewBox="0 0 1528 952" aria-hidden="true"><path d="M0 140C180 40 600 20 900 220C1120 380 1300 400 1528 250V952H0Z" fill="var(--footer)"/></svg>
    <div class="abs foot-mark"></div>
    <div class="abs foot-name">ledgerly</div>
    <svg class="abs" style="left:236px;top:476px" width="30" height="40" viewBox="0 0 30 40" aria-hidden="true"><path d="M15 2C8 2 3 7 3 14c0 9 12 22 12 22s12-13 12-22C27 7 22 2 15 2z" fill="none" stroke="#d7dae3" stroke-width="3"/><circle cx="15" cy="14" r="4" fill="#d7dae3"/></svg>
    <div class="abs foot-address">Ledgerly Ltd<br>48 Kestrel Lane<br>Suite 4<br>Dublin D02 XY45</div>
    <svg class="abs" style="left:236px;top:650px" width="32" height="32" viewBox="0 0 32 32" aria-hidden="true"><circle cx="16" cy="16" r="14" fill="none" stroke="#d7dae3" stroke-width="3"/><path d="M11 9l3 4-2 2c1 2 3 4 5 5l2-2 4 3-2 3c-6-1-11-6-12-12z" fill="#d7dae3"/></svg>
    <div class="abs foot-phone">+00 11 22 333</div>
    <div class="abs foot-rule" style="left:652px;top:468px"></div>
    <div class="abs foot-rule" style="left:1020px;top:468px"></div>
    <div class="abs foot-col" style="left:732px;top:464px">
      <h4>Learn</h4>
      <a>What is Ledgerly?</a><a>Ledgerly Basics</a><a>Technical Analysis</a><a>FAQ's</a><a>Blog</a><a>Support</a>
    </div>
    <div class="abs foot-col" style="left:1100px;top:496px">
      <h4>Explore</h4>
      <a>Features</a><a>Exchanges</a><a>Historical Data</a><a>Ledgerly API</a>
    </div>
    <span class="social" style="left:574px"></span>
    <span class="social" style="left:650px"></span>
    <span class="social" style="left:738px"></span>
    <span class="social" style="left:834px"></span>
    <span class="social" style="left:914px"></span>
  </footer>

</div>
</body>
</html>
```